We are looking for an effective ad to recruit work from home Loan Officers for our Mortgage Brokerage.
Use the following text...
Earn Mortgage Income in your sleep. Its as easy as 1, 2, 3.....
1) Solicit Potential Applicants (Word of Mouth, Email, Social Media etc.)
2) Take Complete Applications & Submit Them
3) Wait to Get Paid.......(Avg. $2,500 per closing)
"You open the door, we'll finish the deal"
No Experience Necessary
No Goals or Quotas
No Office Hours / Work from Home Office
...and We Fully Reimburse ALL LICENSING FEES!!
Email Resume to mwelby@brightharborloans.example
Bright Harbor Lending Group, Inc.
947 W Caldwell Avenue, #318
Baltimore, MD 21230
NMLS #731860
www.brightharborloans.example
Phone (800) 555-0142
Licensed Mortgage Broker in MD and DC since 1997
Target Market(s)
Professionals looking to earn part time income at Loan Officers, preferably with strong social media following.
Industry/Entity Type
Loan
Look and feel

```html
<!DOCTYPE html>
<html lang="en">
<head>
<meta charset="utf-8">
<title>Bright Harbor Lending Group – Loan Officer Recruitment</title>
<link rel="stylesheet" href="https://fonts.googleapis.com/css2?family=Arimo:wght@400;700&family=Raleway:wght@400;500&family=Open+Sans:wght@600&display=swap">
<style>
  :root {
    --sky: #5b9fd2;
    --sky-deep: #3f7fb8;
    --sky-light: #a9d0ee;
    --icon-blue: #3a8fd8;
    --band: #6aa8d4;
    --ink: #2d2d2d;
    --ink-soft: #555b60;
    --rule: #c9cdd1;
    --paper: #ffffff;
    --paper-shade: #eef1f4;
    --head: "Arimo", Arial, sans-serif;
    --body: "Raleway", Arial, sans-serif;
    --foot: "Open Sans", Arial, sans-serif;
  }
  * { margin: 0; padding: 0; box-sizing: border-box; }
  html, body { width: 1019px; height: 1200px; overflow: hidden; }
  body { background: var(--paper); font-family: var(--body); color: var(--ink); }
  .flyer { position: relative; width: 1019px; height: 1200px; overflow: hidden;
    background: linear-gradient(160deg, var(--paper) 40%, var(--paper-shade) 100%); }
  .hero { position: absolute; left: 0; top: 0; width: 1019px; height: 580px; }

  .headline { position: absolute; left: 278px; top: 18px;
    transform: translateX(-50%) scaleX(0.39); transform-origin: 50% 0;
    font-family: var(--head); font-weight: 700; color: #fff; text-align: center;
    font-size: 86px; line-height: 100px; white-space: nowrap; text-transform: uppercase; }

  .brand { position: absolute; left: 814px; top: 74px; transform: translate(-50%, -50%);
    font-family: var(--body); font-weight: 500; font-size: 16px; color: #fff;
    text-align: center; line-height: 20px; width: 190px; }

  .step-icon { position: absolute; left: 239px; width: 44px; height: 40px; }
  .step-line { position: absolute; left: 261px; transform: translate(-50%, -50%);
    white-space: nowrap; text-align: center; }
  .step-title { font-size: 29px; font-weight: 400; line-height: 34px; }
  .step-note { font-size: 18px; line-height: 22px; }
  .rule { position: absolute; left: 56px; width: 413px; height: 2px; background: var(--rule); }

  .tagline { position: absolute; left: 742px; top: 619px;
    transform: translateX(-50%) scaleX(0.55); transform-origin: 50% 0;
    font-family: var(--head); font-weight: 700; font-size: 49px; line-height: 54px;
    color: var(--ink-soft); text-align: center; text-transform: uppercase; white-space: nowrap; }

  .perks { position: absolute; left: 521px; top: 767px; list-style: none; }
  .perks li { position: relative; padding-left: 44px; font-size: 27px; line-height: 33px;
    color: var(--ink-soft); margin-bottom: 10px; letter-spacing: 0.5px; white-space: nowrap; }
  .perks svg { position: absolute; left: 0; top: 6px; }

  .reimburse { position: absolute; left: 492px; top: 994px; transform: translateX(-50%);
    font-size: 30px; line-height: 34px; color: var(--ink-soft); white-space: nowrap; letter-spacing: 0.3px; }

  .footer-rule { position: absolute; left: 0; top: 1041px; width: 1019px; height: 2px; background: #e3e6e9; }
  .contact { position: absolute; top: 1043px; font-family: var(--foot); font-weight: 600; font-style: normal;
    font-size: 18px; line-height: 28px; color: var(--ink); white-space: nowrap; letter-spacing: -0.3px; }
  .contact-left { left: 58px; }
  .contact-mid { left: 513px; top: 1071px; transform: translateX(-50%); text-align: center; }

  .social { position: absolute; left: 742px; top: 1059px; width: 213px; height: 64px;
    border: 2px solid var(--sky-deep); border-radius: 4px; display: flex; align-items: center;
    gap: 10px; padding-left: 14px; font-family: var(--body); font-weight: 500;
    font-size: 18px; line-height: 21px; color: var(--sky-deep); }
  .social-dot { flex: none; width: 30px; height: 30px; background: var(--sky-deep); border-radius: 3px; }

  .band { position: absolute; left: 0; top: 1159px; width: 1019px; height: 41px; background: var(--band);
    color: #fff; font-family: var(--body); font-weight: 500; font-size: 25px; text-align: center; line-height: 41px; }
</style>
</head>
<body>
<main class="flyer">
  <svg class="hero" viewBox="0 0 1019 580" role="img" aria-label="Photo of a businesswoman fanning a handful of dollar bills in a bright blue modern office">
    <defs>
      <linearGradient id="heroTone" x1="0" y1="0" x2="1" y2="1">
        <stop offset="0" stop-color="#4f93c9"/>
        <stop offset="0.55" stop-color="#6aabd9"/>
        <stop offset="1" stop-color="#8cc0e4"/>
      </linearGradient>
      <radialGradient id="heroGlow" cx="0.72" cy="0.62" r="0.4">
        <stop offset="0" stop-color="#f3ede4" stop-opacity="0.8"/>
        <stop offset="1" stop-color="#f3ede4" stop-opacity="0"/>
      </radialGradient>
    </defs>
    <polygon points="0,0 1019,0 1019,526 619,567 0,471" fill="url(#heroTone)"/>
    <polygon points="0,0 1019,0 1019,526 619,567 0,471" fill="url(#heroGlow)"/>
  </svg>

  <h1 class="headline">Earn Mortgage Income<br>In Your Spare Time.<br>Its As Easy As 1, 2, 3...</h1>

  <div class="brand">Bright Harbor Lending Group, Inc.</div>

  <svg class="step-icon" style="top:544px" viewBox="0 0 44 40"><rect width="44" height="40" rx="7" fill="var(--icon-blue)"/><text x="22" y="31" text-anchor="middle" font-family="Arial, sans-serif" font-weight="700" font-size="28" fill="#fff">1</text></svg>
  <h2 class="step-line step-title" style="top:605px">Solicit Potential Applicants</h2>
  <p class="step-line step-note" style="top:640px">(Word of Mouth, Email, Social Media etc.)</p>
  <div class="rule" style="top:667px"></div>

  <svg class="step-icon" style="top:676px" viewBox="0 0 44 40"><rect width="44" height="40" rx="7" fill="var(--icon-blue)"/><text x="22" y="31" text-anchor="middle" font-family="Arial, sans-serif" font-weight="700" font-size="28" fill="#fff">2</text></svg>
  <h2 class="step-line step-title" style="top:740px">Take Complete Applications</h2>
  <h2 class="step-line step-title" style="top:775px">&amp; Submit Them</h2>
  <div class="rule" style="top:805px"></div>

  <svg class="step-icon" style="top:816px" viewBox="0 0 44 40"><rect width="44" height="40" rx="7" fill="var(--icon-blue)"/><text x="22" y="31" text-anchor="middle" font-family="Arial, sans-serif" font-weight="700" font-size="28" fill="#fff">3</text></svg>
  <h2 class="step-line step-title" style="top:879px">Wait to Get Paid...</h2>
  <p class="step-line step-note" style="top:914px">(Avg. $2,500 per closing)</p>

  <p class="tagline">You open the door,<br>we'll finish the deal</p>

  <ul class="perks">
    <li><svg width="36" height="22" viewBox="0 0 36 22"><path d="M1 7h20V1l14 10-14 10v-6H1z" fill="var(--sky-light)" stroke="var(--icon-blue)" stroke-width="1.5"/></svg>No Experience Necessary</li>
    <li><svg width="36" height="22" viewBox="0 0 36 22"><path d="M1 7h20V1l14 10-14 10v-6H1z" fill="var(--sky-light)" stroke="var(--icon-blue)" stroke-width="1.5"/></svg>No Goals or Quotas</li>
    <li><svg width="36" height="22" viewBox="0 0 36 22"><path d="M1 7h20V1l14 10-14 10v-6H1z" fill="var(--sky-light)" stroke="var(--icon-blue)" stroke-width="1.5"/></svg>No Office Hours / Work<br>from Home Office</li>
  </ul>

  <p class="reimburse">...and We Fully Reimburse ALL LICENSING FEES!</p>

  <div class="footer-rule"></div>
  <address class="contact contact-left">
    Bright Harbor Lending Group, Inc.<br>
    947 W Caldwell Avenue, #318<br>
    Baltimore, MD 21230<br>
    NMLS #731860
  </address>
  <address class="contact contact-mid">
    www.brightharborloans.example<br>
    Phone (800) 555-0142<br>
    Email resume to mwelby@brightharborloans.example
  </address>

  <div class="social"><span class="social-dot"></span><span>Like us on<br>FriendSpace</span></div>

  <footer class="band">Licensed Mortgage Broker in MD and DC since 1997</footer>
</main>
</body>
</html>
```